Business Card Design Project

New business cards that encompass our new logo.
Looking for -
Name, Title, Cell Phone, Email, Address (2 lines), Main Phone, Fax, and website.
Reason: I don't like the graphics used to show phone, fax, cell, email, web, and address.....
I like the double sided cards with logo's on the back. I do not like the logos for phone, fax, cell, address, email, or web.

```html
<!DOCTYPE html>
<html lang="en">
<head>
<meta charset="utf-8">
<title>Northpeak Restaurant Supply – Business Card</title>
<link href="https://fonts.googleapis.com/css2?family=Ubuntu:wght@400;500;700&display=swap" rel="stylesheet">
<style>
  :root{
    --stage:#e7e8ea;
    --card:#ffffff;
    --navy:#1f3f73;
    --red:#c12a3f;
    --ink:#3a3a3a;
  }
  html,body{margin:0;padding:0;width:1200px;height:800px;overflow:hidden;background:var(--stage);}
  .stage{width:1200px;height:800px;display:flex;align-items:center;justify-content:center;}
  .card{
    position:relative;width:420px;height:735px;background:var(--card);
    box-shadow:0 6px 24px rgba(0,0,0,.12);overflow:hidden;
    font-family:"Ubuntu",sans-serif;
  }
  .brand{
    position:absolute;top:80px;left:0;right:0;text-align:center;
    color:var(--navy);font-weight:700;
  }
  .brand-mark{width:26px;height:26px;background:var(--red);margin:0 auto 16px;}
  .brand-name{font-size:44px;letter-spacing:2px;line-height:1;}
  .brand-sub{font-size:22px;letter-spacing:3.5px;margin-top:8px;}
  .person{
    position:absolute;top:252px;left:54px;right:54px;
    color:var(--ink);
  }
  .person-name{font-size:20px;font-weight:500;letter-spacing:1px;color:var(--navy);}
  .person-title{font-size:14px;letter-spacing:1.2px;margin-top:4px;}
  .contacts{position:absolute;top:322px;left:40px;right:40px;}
  .row{display:flex;align-items:flex-end;margin-bottom:30px;}
  .row-text{
    flex:1;border-bottom:2px solid var(--red);padding:0 0 8px 14px;
    font-size:15px;letter-spacing:1.2px;color:var(--ink);line-height:1.55;
  }
  .label{display:inline-block;width:44px;color:var(--red);font-weight:500;}
  .marker{
    width:22px;height:22px;background:var(--red);flex:none;margin-bottom:-10px;
  }
  .band{position:absolute;left:0;bottom:0;width:420px;height:90px;}
  .band polygon{fill:var(--navy);}
</style>
</head>
<body>
<div class="stage">
  <div class="card">
    <div class="brand">
      <div class="brand-mark"></div>
      <div class="brand-name">NORTHPEAK</div>
      <div class="brand-sub">RESTAURANT SUPPLY</div>
    </div>

    <div class="person">
      <div class="person-name">Daniel Okafor</div>
      <div class="person-title">Sales Manager</div>
    </div>

    <div class="contacts">
      <div class="row">
        <div class="row-text">2750 Harbor Rd.<br>Suite 4, Fairview 40817</div>
        <div class="marker"></div>
      </div>
      <div class="row">
        <div class="row-text"><span class="label">Main</span>555-210-4471<br><span class="label">Cell</span>555-210-4472</div>
        <div class="marker"></div>
      </div>
      <div class="row">
        <div class="row-text"><span class="label">Fax</span>555-210-4480</div>
        <div class="marker"></div>
      </div>
      <div class="row">
        <div class="row-text">office@northpeaksupply.com<br>www.northpeaksupply.com</div>
        <div class="marker"></div>
      </div>
    </div>

    <svg class="band" viewBox="0 0 420 90" aria-hidden="true">
      <polygon points="0,68 170,68 260,20 420,20 420,90 0,90"/>
    </svg>
  </div>
</div>
</body>
</html>
```